Business Card Design Project

Small privately owned salon.

Industry/Entity Type

Business

Contact Information for Business Card

Hair salon.i would like my logo to be my name , Rosalind Marie. Address and phone can go on the front or back. The back will be where I write their appt.
address-527 Willowbend lane Millbrook, Pa. 16830
Phone- 814-464-3082

```html
<!DOCTYPE html>
<html lang="en">
<head>
<meta charset="utf-8">
<title>Rosalind Marie Hair Salon – Business Cards</title>
<link rel="stylesheet" href="https://fonts.googleapis.com/css2?family=Poiret+One&family=Questrial&display=swap">
<style>
  :root {
    --backdrop: #3a3735;
    --card-light: #f3f3f1;
    --card-dark: #2a2c31;
    --accent: #c8214f;
    --ink: #3b3b3e;
    --ink-on-dark: #d9d9dc;
    --rule: #4a4a4a;
  }
  * { box-sizing: border-box; margin: 0; padding: 0; }
  html, body {
    width: 1200px;
    height: 727px;
    overflow: hidden;
    background: var(--backdrop);
    font-family: "Questrial", "Century Gothic", sans-serif;
  }
  .canvas {
    width: 1200px;
    height: 727px;
    display: flex;
    align-items: center;
    justify-content: center;
    gap: 44px;
  }
  .card {
    position: relative;
    width: 525px;
    height: 300px;
    border-radius: 3px;
    box-shadow: 0 10px 28px rgba(0,0,0,.35);
  }
  .card--appointment { background: var(--card-light); }
  .card--contact { background: var(--card-dark); }

  .brand {
    position: absolute;
    display: flex;
    flex-direction: column;
    align-items: flex-end;
  }
  .brand__row {
    display: flex;
    align-items: center;
    gap: 10px;
  }
  .brand__dot {
    width: 13px;
    height: 13px;
    border-radius: 50%;
    background: var(--accent);
  }
  .brand__name {
    font-family: "Poiret One", "Questrial", sans-serif;
    font-size: 42px;
    line-height: 1;
  }
  .brand__tagline {
    margin-top: 2px;
    margin-right: -6px;
    font-size: 13px;
    letter-spacing: 9px;
    color: var(--accent);
    text-transform: uppercase;
  }
  .card--appointment .brand { top: 62px; right: 80px; }
  .card--appointment .brand__name { color: var(--ink); }
  .card--contact .brand { top: 80px; right: 44px; }
  .card--contact .brand__name { color: var(--ink-on-dark); }

  .appt-form {
    position: absolute;
    inset: 0;
    font-size: 14px;
    color: var(--ink);
  }
  .appt-form__field {
    position: absolute;
    display: flex;
    align-items: flex-end;
    gap: 4px;
  }
  .appt-form__field--name { left: 40px; top: 180px; }
  .appt-form__field--date { left: 170px; top: 232px; }
  .appt-form__line {
    display: inline-block;
    width: 120px;
    height: 14px;
    border-bottom: 1px solid var(--rule);
  }
  .appt-form__field--date .appt-form__line { width: 140px; }
  .appt-form__label {
    position: absolute;
    left: 185px;
    top: 206px;
    color: var(--accent);
    font-size: 15px;
  }

  .contact {
    position: absolute;
    left: 36px;
    top: 165px;
    list-style: none;
    color: var(--ink-on-dark);
    font-size: 15px;
  }
  .contact__item {
    display: flex;
    align-items: center;
    gap: 10px;
    margin-top: 8px;
  }
  .contact__icon { width: 14px; height: 14px; flex: none; }
</style>
</head>
<body>
<main class="canvas">

  <section class="card card--appointment" aria-label="Appointment side">
    <div class="brand">
      <div class="brand__row">
        <span class="brand__dot"></span>
        <span class="brand__name">Rosalind Marie</span>
      </div>
      <span class="brand__tagline">Hair Salon</span>
    </div>
    <div class="appt-form">
      <span class="appt-form__field appt-form__field--name">Name <span class="appt-form__line"></span></span>
      <span class="appt-form__label">Appointment</span>
      <span class="appt-form__field appt-form__field--date">Date <span class="appt-form__line"></span></span>
    </div>
  </section>

  <section class="card card--contact" aria-label="Contact side">
    <div class="brand">
      <div class="brand__row">
        <span class="brand__dot"></span>
        <span class="brand__name">Rosalind Marie</span>
      </div>
      <span class="brand__tagline">Hair Salon</span>
    </div>
    <ul class="contact">
      <li class="contact__item">
        <svg class="contact__icon" viewBox="0 0 14 14" aria-hidden="true">
          <path d="M7 0.5a4.6 4.6 0 0 0-4.6 4.6C2.4 8.6 7 13.5 7 13.5s4.6-4.9 4.6-8.4A4.6 4.6 0 0 0 7 .5z" fill="var(--accent)"/>
          <circle cx="7" cy="5.1" r="1.7" fill="var(--card-dark)"/>
        </svg>
        <span>527 Willowbend lane Millbrook, Pa. 16830</span>
      </li>
      <li class="contact__item">
        <svg class="contact__icon" viewBox="0 0 14 14" aria-hidden="true">
          <path d="M3.2 1h2l1 3-1.4 1.1a7.5 7.5 0 0 0 4.1 4.1L10 7.8l3 1v2c0 .7-.6 1.2-1.3 1.2C5.8 12 2 8.2 2 2.3 2 1.6 2.5 1 3.2 1z" fill="var(--accent)"/>
        </svg>
        <span>814-464-3082</span>
      </li>
    </ul>
  </section>

</main>
</body>
</html>
```